Business Card Design Harlow Airflow Systems

The Business will be centred around supply and installation of Ventilation for domestic homes and warehousing/workshops, and will be marketed as a Eco friendly means of reducing your carbon footprint and reducing energy consumption.Our suppliers will provide a range of products that will ventilate roof spaces and later will branch into to air transfer within homes for cooling and heating other rooms of the home etc.I would like to see colours that would be commensurate with the logo provided and yet not dominate the logo.Final design should convey a Diverse , professional but friendly service that will suit client needs

Target Market(s)

Domestic home owners and warehousing/workshop businesses

Industry/Entity Type

Business

Contact Information for Business Card

Company Name: Harlow Airflow Systems Pty Ltd, ABN: 42 817 350 294, Address: 27 Merrow Tunstead W.A 6084, Email: dale@harlowairflowsystems.com.au, Mobile Number: 0451 862 019

Requirements
Nice to have
• A tract art that commensurate of the logo supplied
Should not have
• Font style that opposes logo design

```html
<!DOCTYPE html>
<html lang="en">
<head>
<meta charset="utf-8">
<title>Harlow Airflow Systems – Business Card</title>
<link rel="stylesheet" href="https://fonts.googleapis.com/css2?family=Source+Sans+3:wght@400;600;700&display=swap">
<style>
  :root {
    --backdrop: #2b2b2d;
    --green: #22a845;
    --green-light: #3cc35e;
    --green-dark: #148a33;
    --maroon: #5a1e1e;
    --white: #ffffff;
    --ink-green: #1f9a3f;
  }
  html, body {
    margin: 0;
    padding: 0;
    width: 1200px;
    height: 871px;
    overflow: hidden;
    background: var(--backdrop);
    font-family: "Source Sans 3", "Myriad Pro", Arial, sans-serif;
  }
  .canvas {
    width: 1200px;
    height: 871px;
    display: flex;
    align-items: center;
    justify-content: center;
    gap: 40px;
  }
  .card {
    position: relative;
    width: 540px;
    height: 330px;
    border-radius: 22px;
    overflow: hidden;
    box-shadow: 0 12px 30px rgba(0,0,0,0.45);
  }
  /* Back side */
  .card-back {
    background: linear-gradient(160deg, var(--green-light) 0%, var(--green) 45%, var(--green-dark) 100%);
  }
  .card-back .brand {
    position: absolute;
    top: 34px;
    right: 34px;
    text-align: right;
    color: var(--white);
  }
  .card-back .brand-name {
    font-size: 30px;
    font-weight: 600;
    letter-spacing: 0.2px;
    margin: 0;
  }
  .card-back .website {
    font-size: 14px;
    font-weight: 600;
    margin: 6px 0 0;
  }
  /* Front side */
  .card-front { background: var(--white); }
  .card-front .swoosh {
    position: absolute;
    inset: 0;
    width: 100%;
    height: 100%;
  }
  .card-front .brand {
    position: absolute;
    top: 62px;
    left: 210px;
    display: flex;
    align-items: center;
    gap: 10px;
  }
  .card-front .brand-dot {
    width: 14px;
    height: 14px;
    border-radius: 50%;
    background: var(--ink-green);
  }
  .card-front .brand-name {
    font-size: 27px;
    font-weight: 600;
    color: var(--ink-green);
    margin: 0;
  }
  .contact {
    position: absolute;
    left: 26px;
    top: 176px;
    margin: 0;
    padding: 0;
    list-style: none;
    color: var(--white);
    font-size: 13.5px;
    line-height: 19px;
  }
  .contact .phone {
    display: flex;
    align-items: center;
    gap: 6px;
  }
  .holder {
    position: absolute;
    right: 30px;
    bottom: 22px;
    text-align: right;
    color: var(--white);
  }
  .holder .name {
    font-size: 21px;
    font-weight: 700;
    margin: 0;
  }
  .holder .role {
    font-size: 14px;
    margin: 2px 0 0;
  }
</style>
</head>
<body>
<main class="canvas">
  <section class="card card-back" aria-label="Card back">
    <div class="brand">
      <p class="brand-name">Harlow Airflow Systems</p>
      <p class="website">www.harlowairflowsystems.com.au</p>
    </div>
  </section>

  <section class="card card-front" aria-label="Card front">
    <svg class="swoosh" viewBox="0 0 540 330" preserveAspectRatio="none" aria-hidden="true">
      <defs>
        <linearGradient id="greenFill" x1="0" y1="0" x2="0" y2="1">
          <stop offset="0" stop-color="#3cc35e"/>
          <stop offset="1" stop-color="#1a9a3b"/>
        </linearGradient>
      </defs>
      <path d="M0,122 C140,112 240,250 540,248 L540,330 L0,330 Z" fill="url(#greenFill)"/>
      <path d="M0,122 C140,112 240,250 540,248" fill="none" stroke="#ffffff" stroke-width="5"/>
      <path d="M0,112 C140,100 250,232 540,236" fill="none" stroke="#22a845" stroke-width="4"/>
      <path d="M250,214 C330,236 420,244 540,238 L540,244 C420,250 330,244 250,214 Z" fill="#5a1e1e"/>
    </svg>

    <div class="brand">
      <span class="brand-dot" aria-hidden="true"></span>
      <p class="brand-name">Harlow Airflow Systems</p>
    </div>

    <ul class="contact">
      <li>ABN: 42 817 350 294</li>
      <li>4/12 Tarrant Road Kelmscott WA 6111</li>
      <li>PO Box 2218, Tunstead WA 6084</li>
      <li class="phone">
        <svg width="9" height="13" viewBox="0 0 9 13" aria-hidden="true"><rect x="0.75" y="0.75" width="7.5" height="11.5" rx="1.5" fill="none" stroke="#fff" stroke-width="1.5"/></svg>
        0451 862 019
      </li>
      <li>dale@harlowairflowsystems.com.au</li>
    </ul>

    <div class="holder">
      <p class="name">Dale Mercer</p>
      <p class="role">Director</p>
    </div>
  </section>
</main>
</body>
</html>
```